Cafe Menu Required

We need a menu for our coffee shop.
I would like something very much the same as what I have attached.

I have attached a word doc with the items needed on the menu.

I have also attached our logo

I would like to print these on A3 size poster

Industry/Entity Type

Cafe

```html
<!DOCTYPE html>
<html lang="en">
<head>
<meta charset="utf-8">
<title>NOVA Cafe Menu</title>
<link rel="stylesheet" href="https://fonts.googleapis.com/css2?family=IM+Fell+DW+Pica+SC&family=PT+Sans:wght@400;700&display=swap">
<style>
  :root {
    --space-deep: #0b0d24;
    --space-mid: #1c1f4f;
    --space-violet: #4a3f86;
    --band-blue: #1f4f9a;
    --ink: #ffffff;
    --rule: rgba(255, 255, 255, 0.55);
    --box-fill: #1a5c96;
    --box-edge: #8fb1d6;
    --brand-red: #d8262c;
  }
  * { margin: 0; padding: 0; box-sizing: border-box; }
  html, body { width: 834px; height: 1200px; overflow: hidden; background: var(--space-deep); }
  .menu {
    position: relative;
    width: 834px;
    height: 1200px;
    overflow: hidden;
    color: var(--ink);
    font-family: "PT Sans", sans-serif;
  }
  .menu__backdrop {
    position: absolute; inset: 0;
    background:
      radial-gradient(ellipse 55% 30% at 55% 58%, rgba(170, 160, 225, 0.55), transparent 70%),
      radial-gradient(ellipse 70% 40% at 40% 40%, rgba(90, 75, 160, 0.6), transparent 75%),
      linear-gradient(180deg, var(--space-deep) 0%, var(--space-mid) 35%, var(--space-violet) 60%, var(--space-mid) 85%, var(--space-deep) 100%);
  }
  .menu__band {
    position: absolute; left: 0; right: 0; bottom: 0; height: 42px;
    background: linear-gradient(180deg, rgba(31, 79, 154, 0) 0%, var(--band-blue) 100%);
  }
  .brand {
    position: absolute; left: 48px; top: 68px;
    display: flex; align-items: center; gap: 8px;
  }
  .brand__dot { width: 22px; height: 22px; border-radius: 50%; background: var(--brand-red); }
  .brand__name { font-weight: 700; font-size: 44px; line-height: 1; color: var(--ink); letter-spacing: 1px; }
  .tagline {
    position: absolute; left: 252px; top: 70px;
    font-family: "IM Fell DW Pica SC", serif;
    font-weight: 400;
    font-size: 42px; line-height: 1; white-space: nowrap;
    transform: scaleX(0.74);
    transform-origin: left top;
  }
  .section { position: absolute; }
  .section__title {
    display: inline-block;
    font-size: 26px; font-weight: 400; line-height: 1.1;
    padding: 0 14px 1px 0;
    border-bottom: 2px solid var(--ink);
    margin-bottom: 6px;
  }
  .price-list { list-style: none; }
  .price-list__item {
    display: flex; justify-content: space-between; align-items: flex-end;
    height: 32px; padding-bottom: 3px;
    font-size: 23px; line-height: 1.1;
    border-bottom: 1px solid var(--rule);
  }
  .price-list__item--tall { height: 64px; }
  .price-list__item--tall .price-list__name { line-height: 32px; }
  .price-list__price { white-space: pre; }
  .section--hot { left: 252px; top: 176px; width: 505px; }
  .section--extras { left: 91px; top: 734px; width: 254px; }
  .section--cold { left: 420px; top: 734px; width: 332px; }
  .feature {
    position: absolute; top: 1000px; height: 106px;
    background: var(--box-fill);
    border: 1px solid var(--box-edge);
    padding: 4px 8px;
    font-size: 19px; line-height: 24px; white-space: nowrap;
  }
  .feature__head { display: flex; justify-content: space-between; }
  .feature--signature { left: 91px; width: 255px; }
  .feature--juice { left: 424px; width: 328px; }
  .social { position: absolute; left: 124px; top: 1138px; display: flex; gap: 40px; }
  .social__tile { width: 36px; height: 36px; border-radius: 5px; background: #4d8fd0; }
  .social__tile--third { background: #c9b79a; margin-left: 6px; }
  .handle { position: absolute; right: 82px; top: 1142px; font-size: 19px; }
</style>
</head>
<body>
<main class="menu">
  <div class="menu__backdrop" role="img" aria-label="Starry night sky with a violet galaxy cloud"></div>
  <div class="menu__band"></div>

  <div class="brand">
    <span class="brand__dot"></span>
    <span class="brand__name">NOVA</span>
  </div>
  <h1 class="tagline">COFFEE – CATERING – FOOD TO GO</h1>

  <section class="section section--hot">
    <h2 class="section__title">HOT BEVERAGES</h2>
    <ul class="price-list">
      <li class="price-list__item"><span class="price-list__name">Espresso</span><span class="price-list__price">3.5</span></li>
      <li class="price-list__item"><span class="price-list__name">Piccolo</span><span class="price-list__price">3.5</span></li>
      <li class="price-list__item"><span class="price-list__name">Short Macchiato</span><span class="price-list__price">4.0</span></li>
      <li class="price-list__item"><span class="price-list__name">Long Macchiato</span><span class="price-list__price">4.5</span></li>
      <li class="price-list__item"><span class="price-list__name">Latte</span><span class="price-list__price">4  /  4.5  /  5.5</span></li>
      <li class="price-list__item"><span class="price-list__name">Cappucinno</span><span class="price-list__price">4  /  4.5  /  5.5</span></li>
      <li class="price-list__item"><span class="price-list__name">Flat White</span><span class="price-list__price">4  /  4.50  /  5.50</span></li>
      <li class="price-list__item"><span class="price-list__name">Long Black</span><span class="price-list__price">4  /  4.50  /  5.50</span></li>
      <li class="price-list__item"><span class="price-list__name">Hot Chocolate</span><span class="price-list__price">4  /  4.50  /  5.50</span></li>
      <li class="price-list__item"><span class="price-list__name">White Hot Chocolate</span><span class="price-list__price">4  /  4.50  /  5.50</span></li>
      <li class="price-list__item"><span class="price-list__name">Mocha</span><span class="price-list__price">4.5  /  5.0  /  6.0</span></li>
      <li class="price-list__item"><span class="price-list__name">White Choc Mocha</span><span class="price-list__price">4.5  /  5.0  /  6.0</span></li>
      <li class="price-list__item"><span class="price-list__name">Chai Latte</span><span class="price-list__price">4.5  /  5.0  /  6.0</span></li>
      <li class="price-list__item"><span class="price-list__name">Dirty Chai</span><span class="price-list__price">5.0  /  5.5  /  6.5</span></li>
      <li class="price-list__item"><span class="price-list__name">Selection of Teas</span><span class="price-list__price">3.8</span></li>
    </ul>
  </section>

  <section class="section section--extras">
    <h2 class="section__title">EXTRAS</h2>
    <ul class="price-list">
      <li class="price-list__item"><span class="price-list__name">Extra Shot</span><span class="price-list__price">0.5</span></li>
      <li class="price-list__item"><span class="price-list__name">Decaf</span><span class="price-list__price">0.5</span></li>
      <li class="price-list__item price-list__item--tall"><span class="price-list__name">Syrups – Caramel/<br>Hazelnut/Vanilla</span><span class="price-list__price">0.5</span></li>
      <li class="price-list__item"><span class="price-list__name">Soy</span><span class="price-list__price">0.5</span></li>
      <li class="price-list__item"><span class="price-list__name">Lactose free</span><span class="price-list__price">0.5</span></li>
    </ul>
  </section>

  <section class="section section--cold">
    <h2 class="section__title">COLD BEVERAGES</h2>
    <ul class="price-list">
      <li class="price-list__item"><span class="price-list__name">Iced Latte</span><span class="price-list__price">4.5</span></li>
      <li class="price-list__item"><span class="price-list__name">Iced Long Black</span><span class="price-list__price">4.5</span></li>
      <li class="price-list__item"><span class="price-list__name">Iced Coffee w/ice cream</span><span class="price-list__price">6.0</span></li>
      <li class="price-list__item"><span class="price-list__name">Iced Chocolate w/ice cream</span><span class="price-list__price">6.0</span></li>
      <li class="price-list__item"><span class="price-list__name">Coffee Frappe</span><span class="price-list__price">6.0</span></li>
      <li class="price-list__item"><span class="price-list__name">Mango Frappe</span><span class="price-list__price">6.0</span></li>
    </ul>
  </section>

  <aside class="feature feature--signature">
    <div class="feature__head"><span>The farshot</span><span>6</span></div>
    <p>2 shots of espresso, a<br>generous scoop of<br>vanilla ice cream and milk</p>
  </aside>

  <aside class="feature feature--juice">
    <div class="feature__head"><span>From the juice bar</span><span>5</span></div>
    <p>create your own orange<br>apple carrot celery kale<br>spinach ginger beets lemon</p>
  </aside>

  <div class="social" aria-label="Social channels">
    <span class="social__tile"></span>
    <span class="social__tile"></span>
    <span class="social__tile social__tile--third"></span>
  </div>
  <p class="handle">@farshotcafe</p>
</main>
</body>
</html>
```